Ashworth Web Design Project

I need the front page and an internal page designed for this client's website. The logo is attached. Obviously the colors have to go with and/or work with the logo colors. I also attached a very rough brochure layout to help you see the direction we're going in with print materials. The rough site map is also attached. I see a slider on the homepage, the art for which I may come back to you to create. This clinic is in a very high end Dallas neighborhood. The hook is that it's a primary care and urgent facility with convenient hours.

I don't know how much this impacts your design, but this will be a Wordpress site and I'm using a framework called Struxo (struxo-demo.example). If Struxo proves to be inflexible, I'll have to get a template that allows me to execute your design.

This site (http://oakbendcareclinic.example) has the type and quality of content I will eventually have on the Ashworth site.

I just revised the brief for this project. I added the site map and added details to the overview and the "Must Have" section. Thank you for revisiting the brief. 

Reason: Christmas was a bad time to end it.

Target Market(s)

Women 25-54 with children living at home, income over $150k/year

Industry/Entity Type

Clinic

Requirements
Must have
• Masthead incorporating the logo
Followed by the primary nav
Slider on the home page below that
Dual nav - 1 with the nav in the attached site map
2 secondary nav with areas of healthcare
There will three blocks under the nav
1. It's about time (with a small blurb less than 50 words.
2. It's about choices (with small blurb)
3. It's about you (with small blurb)
Three footer blocks
patient check in link on every page
"No appointment? No problem" icon on every page

```html
<!DOCTYPE html>
<html lang="en">
<head>
<meta charset="utf-8">
<title>Ashworth Medical</title>
<link rel="stylesheet" href="https://fonts.googleapis.com/css2?family=Dosis:wght@400;500;600&family=Advent+Pro:wght@400;500&family=PT+Sans:wght@400;700&display=swap">
<style>
:root{
  --page-bg:#efefe9;
  --white:#ffffff;
  --topbar:#333333;
  --brand-blue:#175a8f;
  --brand-blue-dark:#0f4a7a;
  --band-light:#79b0da;
  --band-frame:#3d8ac8;
  --active-blue:#1a7cc4;
  --nav-grey-top:#f4f4f4;
  --nav-grey-bottom:#c9c9c9;
  --ink:#333333;
  --muted:#8a8a8a;
  --heading-blue:#1a5c96;
  --footer-navy:#0f3658;
  --footer-deep:#0a2740;
  --footer-link:#7fb6e6;
  --green:#3aa655;
}
*{box-sizing:border-box;margin:0;padding:0}
html,body{width:1185px;height:1200px;overflow:hidden}
body{background:var(--page-bg);font-family:"PT Sans",sans-serif;color:var(--ink);position:relative}
a{text-decoration:none;color:inherit}
.page-column{position:absolute;left:137px;top:0;width:911px;height:1200px;background:var(--white);box-shadow:0 0 6px rgba(0,0,0,.15)}
.top-bar{position:absolute;left:155px;top:0;width:875px;height:36px;background:var(--topbar);display:flex;justify-content:flex-end;align-items:center;padding-right:14px;font-family:"Dosis",sans-serif;font-size:16px;color:#ddd}
.top-bar a{padding:0 12px;border-left:1px solid #555}
.brand{position:absolute;left:155px;top:64px;display:flex;align-items:center;gap:8px}
.brand-mark{width:34px;height:34px;border-radius:50%;background:var(--brand-blue)}
.brand-name{font-family:"PT Sans",sans-serif;font-weight:700;font-size:24px;color:var(--brand-blue)}
.walkin-badge{position:absolute;left:754px;top:51px;width:273px;height:64px;background:var(--brand-blue);border-radius:5px;color:#fff;font-family:"Dosis",sans-serif;font-size:21px;text-align:center;line-height:27px;padding-top:5px;letter-spacing:.5px}
.main-nav{position:absolute;left:155px;top:129px;width:875px;height:54px;background:linear-gradient(var(--nav-grey-top),var(--nav-grey-bottom));display:flex;font-family:"Dosis",sans-serif;font-size:17px;color:#333;letter-spacing:.5px}
.main-nav a{display:flex;align-items:center;justify-content:center;flex:1}
.main-nav a.is-active{flex:0 0 100px;background:linear-gradient(#2a95dc,#0c5fa0);color:#fff}
.hero-band{position:absolute;left:0;top:202px;width:1185px;height:338px;background:var(--band-light)}
.hero-frame{position:absolute;left:122px;top:191px;width:942px;height:338px;background:var(--band-frame)}
.hero-frame::before,.hero-frame::after{content:"";position:absolute;bottom:-10px;border-top:10px solid #1b3a55}
.hero-frame::before{left:0;border-left:15px solid transparent}
.hero-frame::after{right:0;border-right:15px solid transparent}
.hero-slide{position:absolute;left:155px;top:200px;width:875px;height:320px;border:3px solid #1f5f99;background:linear-gradient(90deg,#d9c7a6 0%,#e9d08a 45%,#c98f5b 80%,#8f5a3a 100%)}
.care-nav{position:absolute;left:155px;top:529px;width:875px;height:41px;background:linear-gradient(#2d8fd6,#1468aa);display:flex;font-family:"PT Sans",sans-serif;font-weight:700;font-size:13.5px;color:#fff;border-radius:0 0 4px 4px;overflow:hidden}
.care-nav a{display:flex;align-items:center;padding:0 17px 0 16px;border-right:1px solid #0f4f85;white-space:nowrap}
.care-nav a:last-child{border-right:0}
.promise-panel{position:absolute;left:155px;top:583px;width:875px;height:222px;border:1px solid #d4d4d4;border-radius:5px;background:linear-gradient(#f7f7f7,#ececec);display:flex;padding:14px 0}
.promise{flex:1;padding:0 12px;text-align:center;border-right:1px solid #c9c9c9}
.promise:last-child{border-right:0}
.promise h2{font-family:"Dosis",sans-serif;font-weight:500;font-size:22px;color:var(--heading-blue);letter-spacing:.5px;margin-bottom:8px}
.promise p{font-family:"PT Sans",sans-serif;font-size:12px;line-height:16.4px;color:var(--muted);text-align:justify;height:115px;overflow:hidden}
.btn{display:inline-block;width:109px;height:32px;line-height:30px;border-radius:7px;background:linear-gradient(#4aa6e6,#1766a8);border:1px solid #135a95;color:#fff;font-family:"PT Sans",sans-serif;font-weight:700;font-size:13px;text-align:center}
.promise .btn{margin-top:9px}
.welcome{position:absolute;left:155px;top:830px;width:582px}
.welcome h1{font-family:"Advent Pro",sans-serif;font-weight:400;font-size:29px;color:#555;letter-spacing:1px;margin-bottom:8px}
.welcome-image{float:left;width:293px;height:120px;margin:2px 12px 4px 0;border:1px solid #ddd;background:linear-gradient(90deg,#c9d6e6,#eef2f7 60%,#aebfd6);}
.welcome p{font-size:12px;line-height:16.4px;color:var(--muted);text-align:justify}
.welcome .btn{margin-top:8px}
.services{position:absolute;left:757px;top:834px;width:270px}
.services h2{font-family:"Advent Pro",sans-serif;font-weight:400;font-size:29px;color:#555;letter-spacing:1px;margin-bottom:8px}
.services ul{list-style:none;padding-left:11px}
.services li{font-size:12px;line-height:20px;color:#444;padding-left:15px;position:relative}
.services li::before{content:"";position:absolute;left:0;top:7px;width:6px;height:6px;border-radius:50%;background:#3a95d8}
.site-footer{position:absolute;left:155px;top:1100px;width:875px;height:100px}
.footer-row{display:flex;align-items:center;font-family:"Dosis",sans-serif;font-size:12.5px;color:var(--footer-link)}
.footer-row.upper{height:53px;background:var(--footer-navy);padding-left:17px}
.footer-row.lower{height:47px;background:var(--footer-deep);padding-left:17px}
.footer-brand{color:#fff;font-size:16px;margin-right:13px;font-family:"PT Sans",sans-serif}
.footer-row .sep{margin:0 12px;color:#9fc3e4}
.social{display:flex;gap:10px;margin-left:18px}
.social span{width:14px;height:14px;border-radius:50%;background:#8ab8e0}
.copyright{margin-left:auto;margin-right:24px;color:#fff;font-family:"PT Sans",sans-serif;font-size:11px}
</style>
</head>
<body>
<div class="page-column"></div>

<nav class="top-bar"><a href="#">Blog</a><a href="#">Login</a><a href="#">Register</a></nav>

<div class="brand"><span class="brand-mark"></span><span class="brand-name">AshworthMedical</span></div>

<a class="walkin-badge" href="#">No Appointment ?<br>No Problem !</a>

<nav class="main-nav">
  <a class="is-active" href="#">Home</a><a href="#">About us</a><a href="#">Services</a><a href="#">Staff</a><a href="#">Insurance</a><a href="#">Videos</a><a href="#">Contact us</a>
</nav>

<div class="hero-band"></div>
<div class="hero-frame"></div>
<div class="hero-slide" role="img" aria-label="Slider photo: a doctor listening with a stethoscope to a young patient in a warm-lit exam room"></div>

<nav class="care-nav">
  <a href="#">Immediate Care</a><a href="#">Allergies</a><a href="#">Primary Care</a><a href="#">Women's Health</a><a href="#">Medical Spa Treatments</a><a href="#">Men's Health</a><a href="#">Weight Los</a>
</nav>

<section class="promise-panel">
  <article class="promise"><h2>Its About Time !</h2><p>Lorem Ipsum is simply dummy text of the printing and typesetting industry. Lorem Ipsum has been the industry's standard dummy text ever since the 1500s, when an unknown printer took a galley of type and scrambled it to make a type specimen book. It has survived not only five centuries, but also the leap into</p><a class="btn" href="#">Read More</a></article>
  <article class="promise"><h2>Its About Choices !</h2><p>Lorem Ipsum is simply dummy text of the printing and typesetting industry. Lorem Ipsum has been the industry's standard dummy text ever since the 1500s, when an unknown printer took a galley of type and scrambled it to make a type specimen book. It has survived not only five centuries, but also the leap into</p><a class="btn" href="#">Read More</a></article>
  <article class="promise"><h2>Its About You !</h2><p>Lorem Ipsum is simply dummy text of the printing and typesetting industry. Lorem Ipsum has been the industry's standard dummy text ever since the 1500s, when an unknown printer took a galley of type and scrambled it to make a type specimen book. It has survived not only five centuries, but also the leap into</p><a class="btn" href="#">Read More</a></article>
</section>

<section class="welcome">
  <h1>Welcome to Ashworth Medical</h1>
  <div class="welcome-image" role="img" aria-label="Photo of a puzzle-piece globe beside a stethoscope"></div>
  <p>Lorem Ipsum is simply dummy text of the printing and typesetting industry. Lorem Ipsum has been the industry's standard dummy text ever since the 1500s, when an unknown printer took a galley of type and scrambled it to make a type specimen book. It has survived not only five centuries, but also the leap into electronic typesetting, remaining essentially into electronic type Lorem Ipsum is simply dummy text of the printing and typesetting industry. Lorem Ipsum has</p>
  <a class="btn" href="#">Read More</a>
</section>

<aside class="services">
  <h2>Our Services</h2>
  <ul>
    <li>Minor emergencies</li><li>Routine family medicine</li><li>Allergies &amp; asthma</li><li>Stress &amp; fatigue</li><li>Diabetes</li><li>High cholesterol</li><li>High blood pressure</li><li>Depression</li><li>Headaches</li>
  </ul>
</aside>

<footer class="site-footer">
  <div class="footer-row upper">
    <span class="footer-brand">Ashworth Medical</span>
    <a href="#">Immediate Care</a><span class="sep">|</span><a href="#">Allergies</a><span class="sep">|</span><a href="#">Primary Care</a><span class="sep">|</span><a href="#">Women's Health</a><span class="sep">|</span><a href="#">Medical Spa Treatments</a><span class="sep">|</span><a href="#">Men's Health</a><span class="sep">|</span><a href="#">Weight Los</a>
  </div>
  <div class="footer-row lower">
    <a href="#">Home</a><span class="sep">|</span><a href="#">About us</a><span class="sep">|</span><a href="#">Services</a><span class="sep">|</span><a href="#">Staff</a><span class="sep">|</span><a href="#">Insurance</a><span class="sep">|</span><a href="#">Videos</a><span class="sep">|</span><a href="#">Contact us</a>
    <span class="social"><span></span><span></span><span></span></span>
    <span class="copyright">© 2012 Ashworth Medicals.</span>
  </div>
</footer>
</body>
</html>
```